Business Card Design

Divorce
Collaborative Family Law
Family Dispute Resolution
Family Law Property & Children

Target Market(s)

Australia

Industry/Entity Type

Business

Contact Information for Business Card

Delphine Hartwell
M Laws (Family Law) LLB (Hons) BA (Hons) Grad Dip Med (FDR)
Family Dispute Resolution Provider
Hartwell Family Law
PO Box 4723 Fernleigh Rise 3817
Phone 03 58217000 Fax 03 58217100 Email hartwellfamilylaw@quillnet.example

Colors
f04a51

Requirements
Should not have
• Any reference to
United States or US terminology
the word Company

```html
<!DOCTYPE html>
<html lang="en">
<head>
<meta charset="utf-8">
<title>Hartwell Family Law – Business Card</title>
<link href="https://fonts.googleapis.com/css2?family=Poppins:ital,wght@0,400;0,500;0,600;1,400;1,600;1,700&display=swap" rel="stylesheet">
<style>
  :root {
    --brand-red: #d6001c;
    --ink-black: #111111;
    --paper: #ffffff;
    --text-light: #ffffff;
  }
  html, body {
    margin: 0;
    padding: 0;
    overflow: hidden;
    background: var(--paper);
  }
  .card {
    position: relative;
    width: 1200px;
    height: 750px;
    overflow: hidden;
    background: var(--paper);
    font-family: "Poppins", "Century Gothic", sans-serif;
  }
  .card__shapes {
    position: absolute;
    inset: 0;
    width: 1200px;
    height: 750px;
  }
  .shape--red { fill: var(--brand-red); }
  .shape--black { fill: var(--ink-black); }

  .brand-mark {
    position: absolute;
    margin: 0;
    font-weight: 600;
    font-style: normal;
    line-height: 1.05;
  }
  .brand-mark--top {
    left: 70px;
    top: 118px;
    width: 180px;
    font-size: 27px;
    color: var(--brand-red);
  }
  .brand-mark--panel {
    left: 850px;
    top: 440px;
    width: 330px;
    font-size: 44px;
    color: var(--text-light);
    text-align: center;
  }

  .services {
    position: absolute;
    left: 260px;
    top: 69px;
    margin: 0;
    padding: 0;
    list-style: none;
    color: var(--brand-red);
    font-style: italic;
    font-weight: 700;
    font-size: 43px;
    line-height: 53.5px;
    white-space: nowrap;
  }

  .contact {
    position: absolute;
    left: 38px;
    top: 385px;
    width: 660px;
    color: var(--text-light);
    white-space: nowrap;
  }
  .contact__credentials {
    margin: 0;
    font-size: 21.5px;
    line-height: 30.5px;
    font-weight: 400;
  }
  .contact__name,
  .contact__role {
    font-style: italic;
    font-weight: 700;
  }
  .contact__role { display: inline-block; padding-left: 6px; }
  .contact__lines {
    margin: 13px 0 0 6px;
    padding: 0;
    list-style: none;
    font-size: 30px;
    line-height: 43px;
    font-weight: 400;
  }
</style>
</head>
<body>
  <div class="card">
    <svg class="card__shapes" viewBox="0 0 1200 750" aria-hidden="true">
      <polygon class="shape--red" points="470,0 1200,0 1200,25 497,25"/>
      <polygon class="shape--black" points="0,331 648,331 832,666 0,666"/>
      <polygon class="shape--red" points="660,331 1200,331 1200,666 846,666"/>
    </svg>

    <p class="brand-mark brand-mark--top">Hartwell Family Law</p>

    <ul class="services">
      <li>Divorce</li>
      <li>Collaborative Family Law</li>
      <li>Family Dispute Resolution</li>
      <li>Family Law Property &amp; Children</li>
    </ul>

    <div class="contact">
      <p class="contact__credentials">
        <span class="contact__name">Delphine Hartwell M Laws</span> (Family Law) LLB (Hons) BA<br>
        (Hons) Grad Dip Med (FDR)<br>
        <span class="contact__role">Family Dispute Resolution Provider Hartwell Family Law</span><br>
        PO Box 4723 Fernleigh Rise 3817
      </p>
      <ul class="contact__lines">
        <li>Fax :03 58217100</li>
        <li>Phone:&nbsp; 03 58217000</li>
        <li>Email&nbsp; :&nbsp; hartwellfamilylaw@quillnet.example</li>
      </ul>
    </div>

    <p class="brand-mark brand-mark--panel">Hartwell Family Law</p>
  </div>
</body>
</html>
```